Window Tinting Website Design

We are working with a Window Tinting company in California. They do commercial, residential, and automotive tint.

Some websites for inspiration:
https://www.velmoshadez.com/
https://www.qpridegleam.com/
https://drobfinishx.com/

Thank you for taking the time to consider designing a website for us. We are web developers based in Stockton, CA, USA. Most of our projects go through the same process. Understanding this process may help you win a project with us. We custom-code all of our websites in-house. We don’t have any requirements as to what tools you use for your design, but we ask that you follow these guidelines.

IMAGES:
If you use any images or icons in the design, we ask that you have a link to the asset so we can purchase the image/icon. Most of the designs we submit do not have the customer’s images on them unless they have some great images. Be creative; show us the feeling you are trying to portray with your image choices. Use any royalty-free site you choose. We subscribe to Brenlo and mainly use their images, but we can purchase images outside of Brenlo. PLEASE NOTE: we will not submit designs to clients with watermarks on the images.

FONTS:
We ask that you identify the fonts you’re using in the design. This can be done in a message if you want. We typically use Google Fonts and Brenlo Fonts.

CONTENT:
We're always open to different content and ideas. We often submit designs with stock images so the client can see our vision. We typically take pictures after the website launch to use their images with our vision. Lorem Ipsum is fine for paragraphs, but we ask that you make the Headers with correct English. We want to be able to show the vision and identify the sections of the website.

INSPIRATION:
We typically add a couple of links in the brief of websites we like to help you get started in your design.

REVISIONS:
We do not often ask for revisions of the designs unless we see something in the design that may not appeal to the client. If there are slight changes that we want to make, we do that in the development process.

FEEDBACK:
We rarely give feedback on designs during the design process. We are working on many website projects and do not have the time to provide feedback. We usually respond if your request is well thought out and asks specific questions, but a note asking “feedback, please” usually goes unanswered.

```html
<!DOCTYPE html>
<html lang="en">
<head>
<meta charset="utf-8">
<title>Crestview Window Tinting</title>
<link href="https://fonts.googleapis.com/css2?family=Poppins:wght@400;500;600;700;800&display=swap" rel="stylesheet">
<style>
:root{
  --red:#c50b2e;
  --red-dark:#9e0724;
  --ink:#1d1d1d;
  --text:#444;
  --white:#fff;
  --grey:#f2f2f2;
  --footer:#151515;
  --btn-a:#173b3a;
  --btn-b:#050b0b;
}
*{margin:0;padding:0;box-sizing:border-box}
html,body{width:1200px;height:4936px;overflow:hidden}
body{font-family:"Poppins",sans-serif;color:var(--ink);background:var(--white);position:relative}
.abs{position:absolute}
.photo{position:absolute}

/* header */
.site-header{position:absolute;left:0;top:0;width:1200px;height:112px;background:var(--white);z-index:2}
.brand{position:absolute;left:88px;top:28px;display:flex;align-items:center;gap:10px;font-weight:700;font-size:17px;color:var(--red);line-height:1.1}
.brand-dot{width:44px;height:44px;border-radius:50%;background:var(--red)}
.main-nav{position:absolute;right:80px;top:40px;display:flex;gap:36px;font-size:16px;font-weight:500}
.main-nav a{color:var(--ink);text-decoration:none;padding-bottom:6px}
.main-nav a.active{color:var(--red);border-bottom:3px solid var(--red)}

/* hero */
.hero{position:absolute;left:0;top:0;width:1200px;height:780px;background:linear-gradient(160deg,#3d7ad1 0%,#8fb9e8 38%,#c9dcef 60%,#6b8aa8 80%,#cfd4d6 100%)}
.hero-content{position:absolute;left:88px;top:160px;width:640px;display:flex;flex-direction:column;align-items:flex-start;gap:22px}
.hero-title{color:var(--white);font-size:40px;font-weight:800;line-height:1.2;text-transform:uppercase}
.hero-text{width:400px;color:var(--white);font-size:14px;line-height:1.5}
.btn-dark{display:inline-block;background:linear-gradient(90deg,var(--btn-a),var(--btn-b));color:var(--white);border-radius:40px;font-weight:500;text-decoration:none}
.hero .btn-dark{margin-top:44px;padding:18px 38px;font-size:18px}

/* services */
.services{position:absolute;left:0;top:780px;width:1200px;height:732px;background:var(--white)}
.watermark{position:absolute;left:0;width:1200px;text-align:center;font-weight:800;color:transparent;-webkit-text-stroke:1.5px #f3d5db;text-transform:uppercase;letter-spacing:6px;line-height:1}
.section-title{position:absolute;left:0;width:1200px;text-align:center;font-size:44px;font-weight:700;color:var(--red);text-transform:uppercase;line-height:1.2}
.service-card{position:absolute;top:232px;width:324px;height:420px}
.service-card .card-body{position:absolute;left:0;top:140px;width:324px;height:280px;background:var(--white);border-radius:14px;box-shadow:0 4px 18px rgba(0,0,0,.15)}
.service-card .photo{left:20px;top:0;width:284px;height:200px;clip-path:polygon(14% 0,86% 0,100% 24%,100% 100%,0 100%,0 24%);z-index:1}
.service-card h3{position:absolute;left:0;top:104px;width:324px;text-align:center;color:var(--red);font-size:19px;font-weight:600;text-transform:uppercase}
.service-card p{position:absolute;left:36px;top:140px;width:252px;text-align:center;font-size:15px;line-height:1.45;color:var(--text)}
.service-card .btn-dark{position:absolute;left:100px;top:226px;width:124px;text-align:center;padding:8px 0;font-size:13px}

/* about */
.about{position:absolute;left:0;top:1512px;width:1200px;height:800px;background:var(--red)}
.about .photo{border:5px solid var(--white);border-radius:10px}
.about h2{position:absolute;left:680px;top:232px;color:var(--white);font-size:44px;font-weight:700}
.about p{position:absolute;left:680px;top:328px;width:440px;color:var(--white);font-size:15px;line-height:1.55}
.btn-light{position:absolute;background:var(--white);color:var(--ink);border-radius:40px;font-weight:500;text-align:center;text-decoration:none}
.about .btn-light{left:680px;top:556px;width:208px;padding:12px 0;font-size:18px}

/* process */
.process{position:absolute;left:0;top:2312px;width:1200px;height:648px;background:var(--white)}
.process svg text{font-family:"Poppins",sans-serif}

/* promise band */
.promise{position:absolute;left:0;top:2960px;width:1200px;height:288px;background:var(--red);color:var(--white)}
.promise-list{position:absolute;left:104px;top:44px;list-style:none}
.promise-list li{display:flex;align-items:center;gap:22px;font-size:30px;font-weight:600;text-transform:uppercase;height:78px}
.promise-list svg{width:56px;height:56px}
.divider{position:absolute;left:700px;top:40px;width:2px;height:210px;background:rgba(255,255,255,.8)}
.hours{position:absolute;left:760px;top:40px;width:360px}
.hours h3{font-size:36px;font-weight:600;text-transform:uppercase}
.hours hr{border:0;border-top:2px solid var(--white);margin:22px 0 24px;width:330px}
.hours p{font-size:30px;font-weight:500;line-height:1.9}

/* portfolio */
.portfolio{position:absolute;left:0;top:3248px;width:1200px;height:800px;background:var(--grey)}
.portfolio .photo{border-radius:6px}
.portfolio .btn-red{position:absolute;left:460px;top:656px;width:280px;padding:20px 0;background:var(--red);color:var(--white);border-radius:40px;text-align:center;font-size:21px;font-weight:500;text-decoration:none}

/* testimonials */
.testimonials{position:absolute;left:0;top:4048px;width:1200px;height:512px;background:var(--red)}
.testimonials .section-title{color:var(--white)}
.quote-card{position:absolute;top:192px;width:500px;height:170px}
.quote-card .bubble{position:absolute;left:60px;top:0;width:440px;height:170px;background:var(--white);border-radius:85px 18px 18px 85px}
.quote-card .avatar{position:absolute;left:0;top:-10px;width:190px;height:190px;border-radius:50%;border:8px solid var(--white);background:linear-gradient(160deg,#e9e9e9,#b9bcc2)}
.quote-card .mark{position:absolute;left:-26px;top:50px;width:56px;height:56px;border-radius:50%;background:var(--white);color:var(--ink);font-size:40px;font-weight:700;text-align:center;line-height:66px;box-shadow:0 2px 8px rgba(0,0,0,.2)}
.quote-card p{position:absolute;left:220px;top:18px;width:268px;font-size:13px;line-height:1.45;color:var(--ink)}
.quote-card .who{position:absolute;left:220px;top:110px;font-size:12px;line-height:1.4}
.quote-card .who b{font-weight:600}
.stars{color:#f4b400;letter-spacing:2px;font-size:13px}

/* footer */
.site-footer{position:absolute;left:0;top:4560px;width:1200px;height:376px;background:var(--footer);color:var(--white)}
.footer-nav{position:absolute;left:0;top:74px;width:1200px;display:flex;justify-content:center;gap:36px;font-size:16px}
.footer-nav a{color:var(--white);text-decoration:none}
.contact-item{position:absolute;top:164px;display:flex;gap:16px}
.contact-item .icon{width:46px;height:46px;border-radius:50%;background:var(--red);display:flex;align-items:center;justify-content:center;flex:none}
.contact-item .icon svg{width:22px;height:22px}
.contact-item h4{color:var(--red);font-size:14px;font-weight:600;text-transform:uppercase}
.contact-item p{font-size:13px;line-height:1.5}
.footer-base{position:absolute;left:88px;top:300px;width:1024px;border-top:1px solid #333;padding-top:20px;display:flex;justify-content:space-between;font-size:14px}
.socials{display:flex;gap:16px}
.socials span{width:26px;height:26px;border-radius:50%;border:2px solid var(--white)}
</style>
</head>
<body>

<section class="hero">
  <div class="photo" role="img" aria-label="Glass office tower reflecting blue sky with trees" style="left:0;top:0;width:1200px;height:780px;background:linear-gradient(200deg,rgba(40,70,110,.15),rgba(20,40,60,.35))"></div>
  <div class="hero-content">
    <h1 class="hero-title">Lorem ipsum dolor sit<br>amet, consectetur</h1>
    <p class="hero-text">Lorem ipsum dolor sit amet, consectetur adipiscing elit, sed do eiusmod tempor incididunt ut labore.</p>
    <a class="btn-dark" href="#">Get a Free Estimate</a>
  </div>
</section>

<header class="site-header">
  <div class="brand"><span class="brand-dot"></span><span>Crestview<br>Window Tinting</span></div>
  <nav class="main-nav">
    <a class="active" href="#">Home</a>
    <a href="#">About Us</a>
    <a href="#">Tinting ▾</a>
    <a href="#">Portfolio</a>
    <a href="#">Testimonials</a>
    <a href="#">Contact Us</a>
  </nav>
</header>

<section class="services">
  <div class="watermark" style="top:60px;font-size:110px">Tinting</div>
  <h2 class="section-title" style="top:70px">Our Tinting Services</h2>

  <article class="service-card" style="left:88px">
    <div class="card-body">
      <h3>Automotive Tinting</h3>
      <p>Lorem ipsum dolor sit amet, consectetur adipiscing elit, sed do eiusmod tempor incididunt ut</p>
      <a class="btn-dark" href="#">Learn More</a>
    </div>
    <div class="photo" role="img" aria-label="Tinted sports car in a dark garage" style="background:linear-gradient(150deg,#1b1f1c,#4d6b2a 45%,#a7d52a 60%,#222 85%)"></div>
  </article>

  <article class="service-card" style="left:438px">
    <div class="card-body">
      <h3>Residential Tinting</h3>
      <p>Lorem ipsum dolor sit amet, consectetur adipiscing elit, sed do eiusmod tempor incididunt ut</p>
      <a class="btn-dark" href="#">Learn More</a>
    </div>
    <div class="photo" role="img" aria-label="Modern house with large tinted windows" style="background:linear-gradient(170deg,#c7d6e4,#8e8f92 50%,#4c4e52)"></div>
  </article>

  <article class="service-card" style="left:788px">
    <div class="card-body">
      <h3>Commercial Tinting</h3>
      <p>Lorem ipsum dolor sit amet, consectetur adipiscing elit, sed do eiusmod tempor incididunt ut</p>
      <a class="btn-dark" href="#">Learn More</a>
    </div>
    <div class="photo" role="img" aria-label="Glass office building against the sky" style="background:linear-gradient(160deg,#5e95d6,#b2cbe2 50%,#56708a)"></div>
  </article>
</section>

<section class="about">
  <div class="photo" role="img" aria-label="Tall glass office tower" style="left:104px;top:100px;width:350px;height:480px;background:linear-gradient(170deg,#6fa3dc,#b9cfe3 45%,#3f5876)"></div>
  <div class="photo" role="img" aria-label="White SUV with tinted windows" style="left:290px;top:66px;width:268px;height:284px;background:linear-gradient(160deg,#9ab0c2,#eef0f2 50%,#5b5f64)"></div>
  <div class="photo" role="img" aria-label="Glass building facade" style="left:338px;top:424px;width:264px;height:288px;background:linear-gradient(150deg,#8aaed2,#c8d8e4 50%,#4a5a68)"></div>
  <h2>WHO WE ARE?</h2>
  <p>Lorem ipsum dolor sit amet, consectetur adipiscing elit, sed do eiusmod tempor incididunt ut labore et dolore magna aliqua. Ut enim ad minim lorem ipsum dolor sit amet, consectetur adipiscing elit, sed do eiusmod tempor incididunt ut labore et dolore magna aliqua. Ut enim ad minim lorem ipsum dolor sit amet, consectetur adipiscing elit, sed do eiusmod tempor.</p>
  <a class="btn-light" href="#">Know More</a>
</section>

<section class="process">
  <div class="watermark" style="top:40px;font-size:90px">Process</div>
  <h2 class="section-title" style="top:50px">How We Work</h2>
  <svg class="abs" style="left:0;top:0" width="1200" height="648" viewBox="0 0 1200 648">
    <defs>
      <marker id="arrow" viewBox="0 0 10 10" refX="8" refY="5" markerWidth="7" markerHeight="7" orient="auto"><path d="M0 0 L10 5 L0 10 z" fill="#888"/></marker>
      <g id="node">
        <ellipse rx="94" ry="52" fill="var(--red)"/>
        <ellipse rx="84" ry="43" fill="none" stroke="#fff" stroke-width="2"/>
      </g>
    </defs>
    <g fill="none" stroke="#888" stroke-width="2" marker-end="url(#arrow)">
      <path d="M420 236 Q600 190 770 236"/>
      <path d="M920 294 Q960 340 900 392"/>
      <path d="M770 462 Q730 506 700 512"/>
      <path d="M500 512 Q450 506 420 462"/>
      <path d="M300 394 Q250 340 290 296"/>
    </g>
    <use href="#node" x="320" y="240"/>
    <use href="#node" x="872" y="240"/>
    <use href="#node" x="820" y="432"/>
    <use href="#node" x="600" y="520"/>
    <use href="#node" x="340" y="432"/>
    <g fill="#fff" font-size="17" font-weight="600" text-anchor="middle">
      <text x="320" y="246">GUARANTEE</text>
      <text x="872" y="246">CONSULTATION</text>
      <text x="820" y="438">ESTIMATE</text>
      <text x="600" y="526">INSTALLATION</text>
      <text x="340" y="438">INSPECTION</text>
    </g>
    <rect x="482" y="286" width="236" height="104" rx="20" fill="#fff" stroke="var(--red)" stroke-width="3"/>
    <circle cx="516" cy="338" r="14" fill="var(--red)"/>
    <text x="620" y="330" font-size="20" font-weight="700" fill="var(--red)" text-anchor="middle">CRESTVIEW</text>
    <text x="620" y="356" font-size="20" font-weight="700" fill="var(--red)" text-anchor="middle">TINTING</text>
  </svg>
</section>

<section class="promise">
  <ul class="promise-list">
    <li><svg viewBox="0 0 56 56"><circle cx="28" cy="28" r="25" fill="none" stroke="#fff" stroke-width="3"/><text x="28" y="38" font-family="Poppins,sans-serif" font-size="28" font-weight="700" fill="#fff" text-anchor="middle">$</text></svg>Money Back Guarantee</li>
    <li><svg viewBox="0 0 56 56"><circle cx="28" cy="28" r="25" fill="none" stroke="#fff" stroke-width="3"/><path d="M16 29 L25 38 L41 19" fill="none" stroke="#fff" stroke-width="4" stroke-linecap="round" stroke-linejoin="round"/></svg>Lifetime Warranty</li>
    <li><svg viewBox="0 0 56 56"><circle cx="28" cy="28" r="25" fill="none" stroke="#fff" stroke-width="3"/><path d="M16 29 L25 38 L41 19" fill="none" stroke="#fff" stroke-width="4" stroke-linecap="round" stroke-linejoin="round"/></svg>Certified Installers</li>
  </ul>
  <div class="divider"></div>
  <div class="hours">
    <h3>Working Hours</h3>
    <hr>
    <p>Monday – Friday</p>
    <p>8.00 AM – 5.00 PM</p>
  </div>
</section>

<section class="portfolio">
  <h2 class="section-title" style="top:96px">Portfolio</h2>
  <div class="photo" role="img" aria-label="White jeep parked outdoors" style="left:88px;top:184px;width:372px;height:204px;background:linear-gradient(150deg,#c9d3dc,#f2f2f2 45%,#3a3c40)"></div>
  <div class="photo" role="img" aria-label="Orange sports car" style="left:468px;top:184px;width:260px;height:204px;background:linear-gradient(140deg,#ff8a1a,#f25c05 50%,#2f2f35)"></div>
  <div class="photo" role="img" aria-label="Blue glass skyscraper" style="left:736px;top:184px;width:376px;height:204px;background:linear-gradient(160deg,#3d78c9,#9ec0e6 55%,#2d4d78)"></div>
  <div class="photo" role="img" aria-label="Glass towers seen from below" style="left:88px;top:400px;width:372px;height:208px;background:linear-gradient(170deg,#a6b8c8,#5d7388 50%,#2c3b4a)"></div>
  <div class="photo" role="img" aria-label="Black SUV with tinted windows" style="left:468px;top:400px;width:364px;height:208px;background:linear-gradient(150deg,#8c96a0,#2a2d31 55%,#555)"></div>
  <div class="photo" role="img" aria-label="Colourfully wrapped car" style="left:840px;top:400px;width:272px;height:208px;background:linear-gradient(130deg,#2fb36b,#e8d21c 40%,#d33a8a 70%,#3c5bd6)"></div>
  <a class="btn-red" href="#">More Portfolio</a>
</section>

<section class="testimonials">
  <h2 class="section-title" style="top:80px">Testimonials</h2>
  <article class="quote-card" style="left:112px">
    <div class="bubble"></div>
    <div class="avatar" role="img" aria-label="Customer portrait"></div>
    <div class="mark">“</div>
    <p>Lorem Ipsum, or lipsum as it is sometimes known, is dummy text used in laying out print, graphic or web designs. The passage is attributed</p>
    <div class="who"><b>Mara Ellison</b><br>CEO, Crestview Inc.<br><span class="stars">★★★★★</span></div>
  </article>
  <article class="quote-card" style="left:632px">
    <div class="bubble"></div>
    <div class="avatar" role="img" aria-label="Customer portrait"></div>
    <div class="mark">“</div>
    <p>Lorem Ipsum, or lipsum as it is sometimes known, is dummy text used in laying out print, graphic or web designs. The passage is attributed</p>
    <div class="who"><b>Mara Ellison</b><br>CEO, Crestview Inc.<br><span class="stars">★★★★★</span></div>
  </article>
</section>

<footer class="site-footer">
  <nav class="footer-nav">
    <a href="#">Automotive Tinting</a>
    <a href="#">Commercial Tinting</a>
    <a href="#">Residential Tinting</a>
    <a href="#">Testimonials</a>
    <a href="#">Blog</a>
    <a href="#">Contact Us</a>
  </nav>
  <div class="contact-item" style="left:216px">
    <span class="icon"><svg viewBox="0 0 24 24"><path d="M12 2a7 7 0 0 0-7 7c0 5 7 13 7 13s7-8 7-13a7 7 0 0 0-7-7zm0 9.5A2.5 2.5 0 1 1 12 6.5a2.5 2.5 0 0 1 0 5z" fill="#fff"/></svg></span>
    <div><h4>Location</h4><p>Location Name Sample<br>address here Pin: 123456</p></div>
  </div>
  <div class="contact-item" style="left:520px">
    <span class="icon"><svg viewBox="0 0 24 24"><path d="M6.6 10.8a15 15 0 0 0 6.6 6.6l2.2-2.2a1 1 0 0 1 1-.25 11.4 11.4 0 0 0 3.6.57 1 1 0 0 1 1 1V20a1 1 0 0 1-1 1A17 17 0 0 1 3 4a1 1 0 0 1 1-1h3.5a1 1 0 0 1 1 1c0 1.25.2 2.45.57 3.57a1 1 0 0 1-.25 1z" fill="#fff"/></svg></span>
    <div><h4>Call Us</h4><p>+1 209 555 0142<br>+1 209 555 0187</p></div>
  </div>
  <div class="contact-item" style="left:836px">
    <span class="icon"><svg viewBox="0 0 24 24"><rect x="3" y="5" width="18" height="14" rx="2" fill="#fff"/><path d="M3 7l9 6 9-6" fill="none" stroke="#c50b2e" stroke-width="2"/></svg></span>
    <div><h4>Email</h4><p>hello@crestviewtint.com</p></div>
  </div>
  <div class="footer-base">
    <span>Copyright @ 2023 All rights reserved</span>
    <div class="socials"><span></span><span></span><span></span><span></span></div>
  </div>
</footer>

</body>
</html>
```